Logo & Graphic Design for Children's Event

We need help designing the logo and marketing materials for our summer children's event "Star Parade". This program is for children ages 5-10 and should have a bold, fun feel to it. I would like a strong logo that is the primary feature of the design with additional supporting artwork elements that can be used flexibly in a variety of formats and mediums. I would like the design to capture the overall feel of the event. This event will be themed like a TV game show/variety show and should reflect this vibe.

This design will be used for outside marketing and branding and needs to be provided in a vector format. The types of mediums it would be used on is yard signs, banners, door hangers, social media, etc. (Samples of materials from previous events included in the uploaded files to help you get a feel for the quality and tone that we aim for with this event.)

Target Market(s)

Families with children ages 5-10

Industry/Entity Type

Church

Requirements
Must have
• - Strong logo that communicates the feel of the event and includes the name "Star Parade". - Flexible supporting artwork elements that can be used in a variety of mediums. - Must use fonts that are available from free, open sources or can be provided upon delivery of completed project. - Must be kid and family friendly - Event date June 10-14 must be included - Event time 6:30-8:30pm included - Include our church logo attached - Event web address Brightpathhollow.com/KDC
Nice to have
• - A themed background that could be adapted for use on powerpoint.
Should not have
• - Any content that is scary, violent or not suitable for an audience of children.

```html
<!DOCTYPE html>
<html lang="en">
<head>
<meta charset="utf-8">
<title>Star Parade – Summer Kids Event</title>
<link rel="stylesheet" href="https://fonts.googleapis.com/css2?family=Sniglet:wght@800&family=Questrial&family=Nunito:wght@800&display=swap">
<style>
  :root {
    --page: #ffffff;
    --mint: #20f0a4;
    --ink: #111111;
    --burst-red: #f5123f;
    --burst-pink: #ff4f8a;
    --screen-cream: #fdfbd6;
    --tv-yellow: #f6e51c;
    --title-blue: #3b2fe0;
    --title-green: #7bd43a;
    --title-orange: #ff5a1a;
    --url-blue: #3a1ff0;
    --url-edge: #6a1fc0;
  }
  html, body {
    margin: 0;
    padding: 0;
    overflow: hidden;
    background: var(--page);
  }
  .canvas {
    position: relative;
    width: 1200px;
    height: 1200px;
    background: var(--page);
    overflow: hidden;
  }
  .card {
    position: absolute;
    left: 61px;
    top: 70px;
    width: 1080px;
    height: 1030px;
    background: var(--mint);
    border: 3px solid var(--ink);
    border-radius: 52px;
    box-sizing: border-box;
  }
  .showcase-art {
    position: absolute;
    left: 150px;
    top: 110px;
    width: 940px;
    height: 920px;
    border-radius: 46% 54% 50% 50% / 52% 46% 54% 48%;
    background: radial-gradient(ellipse at 52% 50%,
      var(--screen-cream) 0%,
      var(--screen-cream) 22%,
      var(--tv-yellow) 32%,
      var(--burst-pink) 46%,
      var(--burst-red) 78%);
  }
  .title {
    position: absolute;
    margin: 0;
    font-family: "Sniglet", "Comic Sans MS", cursive, sans-serif;
    font-weight: 800;
    color: var(--title-blue);
    -webkit-text-stroke: 3px var(--title-green);
    paint-order: stroke fill;
    text-shadow: 6px 6px 0 var(--title-orange);
    letter-spacing: 2px;
    line-height: 1;
    white-space: nowrap;
    transform-origin: center;
  }
  .title-top {
    left: 520px;
    top: 470px;
    font-size: 100px;
    transform: translate(-50%, -50%) rotate(-26deg);
  }
  .title-bottom {
    left: 640px;
    top: 668px;
    font-size: 92px;
    transform: translate(-50%, -50%) rotate(-24deg);
  }
  .event-details {
    position: absolute;
    left: 582px;
    top: 546px;
    transform: translate(-50%, -50%);
    text-align: center;
    font-family: "Questrial", "Century Gothic", sans-serif;
    color: var(--ink);
    line-height: 1.25;
  }
  .event-date {
    display: block;
    font-size: 32px;
  }
  .event-time {
    display: block;
    font-size: 22px;
    margin-top: 6px;
  }
  .church-mark {
    position: absolute;
    left: 660px;
    top: 748px;
    display: flex;
    align-items: center;
    gap: 6px;
    font-family: "Questrial", "Century Gothic", sans-serif;
    font-size: 15px;
    color: var(--ink);
  }
  .church-dot {
    width: 26px;
    height: 26px;
    border-radius: 50%;
    background: var(--ink);
  }
  .web-address {
    position: absolute;
    left: 0;
    width: 1200px;
    top: 1035px;
    margin: 0;
    text-align: center;
    font-family: "Nunito", "Century Gothic", sans-serif;
    font-weight: 800;
    font-size: 60px;
    color: var(--url-blue);
    -webkit-text-stroke: 2px var(--url-edge);
    line-height: 1;
  }
</style>
</head>
<body>
  <main class="canvas">
    <section class="card">
    </section>

    <div class="showcase-art" role="img"
         aria-label="Red comic starburst behind a yellow retro television set, with a smiling cartoon boy on the left and a cartoon girl with curly hair on the right"></div>

    <h1 class="title title-top">STAR</h1>

    <p class="event-details">
      <span class="event-date">June 10-14</span>
      <span class="event-time">6:30-8:30 p.m.</span>
    </p>

    <p class="title title-bottom">PARADE</p>

    <div class="church-mark">
      <span class="church-dot"></span>
      <span class="church-name">Bright Path</span>
    </div>

    <p class="web-address">Brightpathhollow.com/KDC</p>
  </main>
</body>
</html>
```